Business card design for crowd sourced review site.

I need a business card magnet design for an online, crowd-sourced, restaurant review site strictly for Kosher restaurants.
It is similar to WanderNotes but catering to a very particular crowd.
The markets it will be distributed in are flooded with business card fridge magnets so this needs to be eye-catching and unique. The Business name is PlateRanker
The website isnt finished but you can see the basic setup here
http://dining.brevtalo.com/

The second image i included is another logo design I liked and was thinking about using and decided I will probably also make a SECOND custom cut business card in the shape of that icon. Bonus if you can throw that in also.

Target Market(s)

Jewish consumers aged 20-35

Industry/Entity Type

Business

Contact Information for Business Card

see description.
Design should not be too crowded and should in eye-catching. Will mainly be used as fridge magnets.

Requirements
Must have
• Website address. logo.
Nice to have
• tagline. (The Definitive guide to kosher dining for the Kosher consumer)
• Im not a professional but I personally think the color blue goes along with this concept. ill leave it to you to decide.
Should not have
• any religious symbols.

```html
<!DOCTYPE html>
<html lang="en">
<head>
<meta charset="utf-8">
<title>PlateRanker — Business Card</title>
<link rel="stylesheet" href="https://fonts.googleapis.com/css2?family=Cabin:wght@400;500&family=Kalam:wght@400&display=swap">
<style>
  :root {
    --page-bg: #e9e4dc;
    --card-dark: #120c0a;
    --photo-deep: #1c0f0b;
    --photo-mid: #5a2416;
    --photo-warm: #8c3a22;
    --photo-accent: #a44a2a;
    --text-light: #f3eee8;
    --band-dark: rgba(12, 8, 7, 0.72);
    --logo-dot: #c0262b;
  }
  html, body {
    margin: 0;
    padding: 0;
    width: 1200px;
    height: 780px;
    overflow: hidden;
    background: var(--page-bg);
  }
  .canvas {
    position: relative;
    width: 1200px;
    height: 780px;
    display: flex;
    align-items: center;
    justify-content: center;
  }
  .business-card {
    position: relative;
    width: 1050px;
    height: 600px;
    background: var(--card-dark);
    overflow: hidden;
    box-shadow: 0 10px 30px rgba(0, 0, 0, 0.25);
  }
  .food-photo {
    position: absolute;
    inset: 0;
    background:
      radial-gradient(ellipse 38% 45% at 62% 38%, var(--photo-accent) 0%, transparent 70%),
      radial-gradient(ellipse 30% 40% at 82% 70%, var(--photo-warm) 0%, transparent 72%),
      radial-gradient(ellipse 34% 40% at 38% 62%, var(--photo-mid) 0%, transparent 75%),
      linear-gradient(120deg, var(--photo-deep) 0%, #2b150e 45%, #3a1a10 70%, var(--photo-deep) 100%);
  }
  .food-photo::after {
    content: "";
    position: absolute;
    inset: 0;
    background: linear-gradient(90deg, rgba(10, 6, 5, 0.55) 0%, rgba(10, 6, 5, 0.1) 45%, rgba(10, 6, 5, 0.2) 100%);
  }
  .brand {
    position: absolute;
    left: 70px;
    bottom: 90px;
    color: var(--text-light);
  }
  .brand-mark {
    display: flex;
    align-items: center;
    gap: 16px;
  }
  .brand-dot {
    width: 22px;
    height: 22px;
    border-radius: 50%;
    background: var(--logo-dot);
  }
  .brand-name {
    font-family: "Cabin", sans-serif;
    font-weight: 500;
    font-size: 64px;
    letter-spacing: 1px;
    color: var(--text-light);
    line-height: 1;
  }
  .tagline {
    margin: 14px 0 0;
    font-family: "Cabin", sans-serif;
    font-weight: 400;
    font-size: 30px;
    letter-spacing: 0.5px;
    color: var(--text-light);
  }
  .web-band {
    position: absolute;
    right: 0;
    top: 250px;
    width: 470px;
    height: 70px;
    background: var(--band-dark);
    display: flex;
    align-items: center;
    justify-content: center;
  }
  .web-address {
    font-family: "Kalam", cursive;
    font-size: 28px;
    color: var(--text-light);
    letter-spacing: 0.5px;
  }
</style>
</head>
<body>
  <main class="canvas">
    <section class="business-card">
      <div class="food-photo" role="img" aria-label="Close-up photograph of grilled steaks and stuffed peppers with green onion on a round barbecue grill"></div>
      <div class="web-band">
        <span class="web-address">http://dining.brevtalo.com/</span>
      </div>
      <div class="brand">
        <div class="brand-mark">
          <span class="brand-dot" aria-hidden="true"></span>
          <span class="brand-name">PlateRanker</span>
        </div>
        <p class="tagline">The Definitive guide to kosher dining for the Kosher consumer</p>
      </div>
    </section>
  </main>
</body>
</html>
```